Wedding Postcard Design

We want to design a postcard using our photo's from our wedding and send the postcards as 'Thank You's' to the guests from our wedding. On the front we would like to use the 3 x photos we have uploaded and perhaps with white boarders and on the back just lines for the addresses.
Ideally we would like them slightly larger size than the standard postcard if possible.
Updates

Sorry for the change however we feel 5 photos is too many and too crowded as I am sure you would agree.  

Can we possibly reduce it to 3 photos using the following 3:

- black and white photo
- photo with the beach behind us
- close up photo on the wharf where he is standing behind me and there is a little yellow boat behind us

 

                                                                 

Target Market(s)

Our friends

Industry/Entity Type

Wedding

```html
<!DOCTYPE html>
<html lang="en">
<head>
<meta charset="utf-8">
<title>Wedding Thank You Postcard</title>
<link href="https://fonts.googleapis.com/css2?family=Great+Vibes&family=Arimo:wght@400;700&display=swap" rel="stylesheet">
<style>
  :root {
    --backdrop: #efece9;
    --front-top: #f5f5f5;
    --front-bottom: #e3e3e3;
    --back-paper: #ffffff;
    --pink-light: #d894c4;
    --pink-deep: #c65ea3;
    --blue: #1b9ee2;
    --blue-light: #5fcbf0;
    --ink: #4a4a4a;
    --rule: #8d7dc4;
    --frame: #ffffff;
  }
  * { box-sizing: border-box; margin: 0; padding: 0; }
  html, body { width: 1200px; height: 438px; overflow: hidden; }
  body { background: var(--backdrop); position: relative; font-family: "Arimo", Arial, sans-serif; }

  .postcard {
    position: absolute; top: 32px; width: 560px; height: 374px; overflow: hidden;
    box-shadow: 0 2px 8px rgba(0,0,0,.18);
  }
  .postcard--front { left: 29px; background: linear-gradient(180deg, var(--front-top), var(--front-bottom)); }
  .postcard--back { left: 612px; background: var(--back-paper); }
  .postcard__waves { position: absolute; inset: 0; width: 560px; height: 374px; }

  .photo {
    position: absolute; border: 5px solid var(--frame);
    box-shadow: 0 3px 10px rgba(0,0,0,.35);
  }
  .photo--beach { left: 71px; top: 107px; width: 106px; height: 175px;
    background: linear-gradient(180deg, #7fa9d6 0%, #b9cfe6 35%, #6d8fa6 50%, #e8ecef 62%, #5f8a3c 78%, #4c7330 100%); }
  .photo--portrait { left: 178px; top: 89px; width: 211px; height: 211px; z-index: 2;
    background: linear-gradient(160deg, #3c3c3c 0%, #6b6b6b 40%, #9a9a9a 65%, #4a4a4a 100%); }
  .photo--wharf { left: 390px; top: 107px; width: 107px; height: 175px;
    background: linear-gradient(180deg, #86b3e3 0%, #c6dcf0 38%, #7f9fb4 55%, #b9a68c 80%, #8a7a66 100%); }

  .front-greeting {
    position: absolute; left: 39px; top: 322px; color: #fff;
    font-family: "Great Vibes", cursive; font-size: 35px; font-weight: 400; line-height: 1.2;
  }

  .floral-spray {
    position: absolute; left: 4px; top: 16px; width: 220px; height: 124px;
    background: radial-gradient(ellipse at 45% 30%, rgba(226,84,108,.35), rgba(255,255,255,0) 70%);
  }
  .back-greeting { position: absolute; left: 20px; top: 152px; color: var(--ink); font-family: "Great Vibes", cursive; }
  .back-greeting__main { display: block; font-size: 43px; line-height: 1.1; }
  .back-greeting__sub { display: block; font-size: 31px; margin: 6px 0 0 5px; line-height: 1.1; }

  .divider { position: absolute; left: 280px; top: 64px; width: 1px; height: 246px; background: var(--rule); }
  .address-lines { position: absolute; left: 326px; top: 151px; width: 212px; list-style: none; }
  .address-lines li { height: 1px; background: var(--rule); margin-bottom: 26.5px; }

  .indicia {
    position: absolute; left: 492px; top: 78px; width: 46px; height: 47px;
    border: 1px solid #333; text-align: center; color: #222;
    font-size: 5.6px; line-height: 1.3; padding-top: 4px;
  }
  .indicia strong { font-size: 7px; display: block; line-height: 1.2; }
</style>
</head>
<body>

<section class="postcard postcard--front">
  <svg class="postcard__waves" viewBox="0 0 560 374" aria-hidden="true">
    <defs>
      <linearGradient id="pinkFront" x1="0" x2="1">
        <stop offset="0" stop-color="#d894c4"/><stop offset="1" stop-color="#c65ea3"/>
      </linearGradient>
    </defs>
    <path d="M0,0 H560 V54 C470,64 380,44 280,30 C180,18 80,22 0,34 Z" fill="url(#pinkFront)"/>
    <path d="M0,34 C80,22 180,18 280,30 C200,24 100,28 0,46 Z" fill="#1b9ee2"/>
    <path d="M280,30 C380,44 470,64 560,54 V58 C470,66 400,52 280,30 Z" fill="#5fcbf0"/>
    <path d="M0,330 C120,318 260,336 380,348 C460,356 520,346 560,332 V374 H0 Z" fill="url(#pinkFront)"/>
    <path d="M0,322 C120,310 240,326 330,340 C230,326 110,318 0,332 Z" fill="#5fcbf0"/>
    <path d="M300,338 C400,352 480,350 560,326 V338 C480,358 400,358 300,338 Z" fill="#1b9ee2"/>
  </svg>
  <div class="photo photo--beach" role="img" aria-label="Photo of the couple on the grass with the beach behind them"></div>
  <div class="photo photo--portrait" role="img" aria-label="Black and white photo of the couple walking among trees"></div>
  <div class="photo photo--wharf" role="img" aria-label="Photo of the couple on the wharf with the water behind them"></div>
  <p class="front-greeting">Thank you</p>
</section>

<section class="postcard postcard--back">
  <svg class="postcard__waves" viewBox="0 0 560 374" aria-hidden="true">
    <defs>
      <linearGradient id="pinkBack" x1="0" x2="1">
        <stop offset="0" stop-color="#d894c4"/><stop offset="1" stop-color="#c65ea3"/>
      </linearGradient>
    </defs>
    <path d="M0,0 H560 V48 C470,58 380,40 280,26 C180,14 80,16 0,26 Z" fill="url(#pinkBack)"/>
    <path d="M0,26 C80,16 180,14 280,26 C200,20 100,22 0,38 Z" fill="#1b9ee2"/>
    <path d="M380,44 C470,60 520,56 560,48 V52 C500,62 450,58 380,44 Z" fill="#5fcbf0"/>
    <path d="M0,330 C120,318 260,336 380,348 C460,356 520,346 560,332 V374 H0 Z" fill="url(#pinkBack)"/>
    <path d="M0,322 C120,310 240,326 330,340 C230,326 110,318 0,332 Z" fill="#5fcbf0"/>
    <path d="M300,338 C400,352 480,350 560,326 V338 C480,358 400,358 300,338 Z" fill="#1b9ee2"/>
  </svg>
  <div class="floral-spray" role="img" aria-label="Illustration of hanging red and pink flowers with curling vines and butterflies"></div>
  <p class="back-greeting">
    <span class="back-greeting__main">Thank you</span>
    <span class="back-greeting__sub">for attending</span>
  </p>
  <div class="divider"></div>
  <ul class="address-lines">
    <li></li><li></li><li></li><li></li>
  </ul>
  <div class="indicia">PRESORTED<br>LOCAL<br>POSTAGE<strong>PAID</strong>AREA MAIL</div>
</section>

</body>
</html>
```